Micro-Marketing and Vending Brochure

I am looking for an elegant, fun, eye catching brochure that will highlight my new business to protential clients in the Hotel, College/University and Hospital industry. please find pictures of Micro-Markets on line and on my website, to make a fun, professional and elegant design, use color scheme from website, and logo and a few picture will be attach to this email. This is a new business and i would like to represent my company in the best possible way, please take time with this project, color, front and wording is very important along with pics. I have a image of a micro-Market please take out the BRISKO and place file logo of TORN..please let me know if more information is needed for this project to be successful

```html
<!DOCTYPE html>
<html lang="en">
<head>
<meta charset="utf-8">
<title>Orvia Markets – Brochure</title>
<link href="https://fonts.googleapis.com/css2?family=Montserrat:wght@400;600;700;800&family=Didact+Gothic&display=swap" rel="stylesheet">
<style>
  :root{
    --purple:#9b8bc6;
    --purple-soft:#b3a3cf;
    --yellow:#f3d45a;
    --yellow-soft:#fbeeb0;
    --sky:#cfe6f5;
    --ink:#4a4a4a;
    --ink-soft:#6d6d6d;
    --paper:#ffffff;
    --stage:#ebe8ef;
  }
  *{margin:0;padding:0;box-sizing:border-box}
  html,body{width:1200px;height:1200px;overflow:hidden;background:var(--stage)}
  body{position:relative;font-family:"Didact Gothic",sans-serif;color:var(--ink)}
  .spread{position:absolute;left:0;width:1200px;height:424px;overflow:hidden}
  .spread--inside{top:196px;background:var(--paper)}
  .spread--outside{top:642px}
  .abs{position:absolute}

  /* inside left panel */
  .benefits{left:48px;top:45px;width:170px;list-style:none}
  .benefits li{height:13px;margin-bottom:6px;font-size:8.5px;line-height:13px;padding-left:4px;
    background:linear-gradient(90deg,var(--yellow) 0%,var(--yellow-soft) 70%,rgba(255,255,255,0) 100%)}
  .intro{left:48px;top:112px;width:170px;font-size:7.6px;line-height:10.2px;text-align:justify;color:var(--ink-soft)}
  .intro .tag{display:inline-block;border:1px solid var(--purple);color:var(--purple);font-size:11px;line-height:12px;padding:0 2px;float:left;margin:0 4px 0 0}
  .intro strong{color:var(--purple);font-family:"Montserrat",sans-serif;font-weight:700}
  .photo{border-radius:0}
  .photo--produce{left:48px;top:168px;width:170px;height:64px;
    background:linear-gradient(90deg,#e7cfa8 0%,#cbb4d9 18%,#7a9c3a 22%,#d7a23a 50%,#b8412f 75%,#6f8c2e 100%)}
  .section-title{left:48px;top:246px;font-size:12.5px;color:var(--purple);letter-spacing:.2px}
  .section-title b{font-family:"Montserrat",sans-serif;font-weight:700}
  .kiosk-copy{left:48px;top:264px;width:170px;font-size:7.6px;line-height:10.2px;text-align:justify;color:var(--ink-soft)}
  .kiosk-copy .initial{float:left;width:16px;height:16px;border:1px solid var(--purple);color:var(--purple);font-size:12px;line-height:14px;text-align:center;margin:1px 4px 0 0}
  .photo--shopper{left:48px;top:309px;width:170px;height:69px;
    background:linear-gradient(90deg,#e7cfa8 0%,#cbb4d9 22%,#2e3b4a 30%,#6d7d8c 60%,#d9cfc4 80%,#2b2f35 100%)}

  /* inside middle panel */
  .facts-panel{left:266px;top:0;width:334px;height:424px;
    background:linear-gradient(160deg,#f4f3f6 0%,#ecebf0 45%,#f3f2f5 100%)}
  .facts-head{left:0;width:334px;text-align:center;color:var(--purple)}
  .facts-head--cool{top:69px;font-size:12.5px}
  .facts-head--cool b{font-family:"Montserrat",sans-serif;font-weight:700}
  .facts-head--fact{top:94px;font-size:12px}
  .fact{left:48px;width:237px;border:1px solid #c9bfe0;display:flex;align-items:center;justify-content:center;text-align:center;font-size:7.6px;line-height:10px;color:var(--ink-soft);padding:10px 16px 0}
  .fact b{color:var(--purple);font-family:"Montserrat",sans-serif}
  .fact--1{top:125px;height:41px}
  .fact--2{top:186px;height:49px}
  .fact--3{top:254px;height:50px}
  .q{left:156px;width:22px;height:22px;background:var(--purple);color:#fff;font-family:"Montserrat",sans-serif;font-weight:700;font-size:11px;line-height:22px;text-align:center}
  .q--1{top:114px}.q--2{top:175px}.q--3{top:243px}
  .cta{left:0;top:320px;width:334px;text-align:center;font-family:"Montserrat",sans-serif;font-weight:600;font-size:7.4px;line-height:10px;color:var(--ink-soft)}
  .site{left:0;top:345px;width:334px;text-align:center;font-family:"Montserrat",sans-serif;font-weight:600;font-size:7.8px;color:var(--purple)}

  /* inside right half */
  .photo--market{left:600px;top:16px;width:600px;height:252px;
    background:linear-gradient(180deg,#111 0%,#1b1b1b 18%,#3a3532 45%,#2a2a2a 70%,#9a9a9a 86%,#ffffff 100%)}
  .lead{left:648px;top:278px;width:500px;font-size:7.8px;color:var(--ink-soft);line-height:14px}
  .lead .initial{display:inline-block;width:14px;height:15px;border:1px solid var(--purple);color:var(--purple);font-size:11px;line-height:13px;text-align:center;margin-right:4px;vertical-align:middle}
  .system-title{left:648px;top:303px;font-size:12px;color:var(--yellow)}
  .system-title b{font-family:"Montserrat",sans-serif;font-weight:700;color:#f0b82e}
  .features{list-style:none;top:326px}
  .features li{height:15px;margin-bottom:4px;font-size:7.8px;line-height:15px;padding-left:15px;position:relative;
    background:linear-gradient(90deg,var(--sky) 0%,rgba(207,230,245,.35) 70%,rgba(255,255,255,0) 100%)}
  .features li::before{content:"";position:absolute;left:2px;top:3px;width:9px;height:9px;background:#fff;border-radius:0 6px 0 6px}
  .features b{font-family:"Montserrat",sans-serif;font-weight:700;color:#222}
  .features--left{left:648px;width:160px}
  .features--right{left:826px;width:320px}

  /* outside back cover */
  .back-cover{left:0;top:0;width:600px;height:424px;background:var(--purple-soft)}
  .brand-mark{left:0;top:284px;width:600px;display:flex;justify-content:center;align-items:center;gap:8px}
  .brand-mark .square{width:24px;height:24px;background:var(--sky)}
  .brand-mark .name{font-family:"Montserrat",sans-serif;font-weight:700;font-size:20px;color:#fff;letter-spacing:2px}
  .contact-title{left:0;top:345px;width:600px;text-align:center;font-family:"Montserrat",sans-serif;font-weight:700;font-size:11.5px;color:#fff}
  .contact-line{left:0;top:365px;width:600px;text-align:center;font-size:11.5px;color:#fff}
  .contact-line b{font-family:"Montserrat",sans-serif;font-weight:700}

  /* outside front cover */
  .photo--people{left:600px;top:0;width:600px;height:424px;
    background:linear-gradient(120deg,#5a3b2a 0%,#b07a55 30%,#f2d7b0 50%,#e6b48a 65%,#9b6d52 85%,#4d5a46 100%)}
  .headline-box{left:600px;top:120px;width:204px;height:134px;background:#fff;border:3px solid var(--sky);padding:18px 0 0 26px}
  .headline-box .l1{font-family:"Montserrat",sans-serif;font-weight:800;font-size:27px;line-height:32px;color:var(--yellow)}
  .headline-box .l2{font-family:"Montserrat",sans-serif;font-weight:800;font-size:27px;line-height:32px;color:var(--purple)}
  .headline-box .l3{font-size:21px;line-height:26px;color:var(--ink-soft)}
  .markets-frame{left:804px;top:142px;width:208px;height:136px;border:3px solid var(--sky);border-left:none}
  .tail{left:752px;top:252px}
  .market{height:18px;font-size:11.5px;line-height:18px;color:#fff;padding:0 6px 0 5px;display:inline-block}
  .market--hotels{left:806px;top:157px;background:var(--purple)}
  .market--colleges{left:806px;top:183px;background:var(--yellow)}
  .market--hospitals{left:806px;top:209px;background:#b79bc6}
  .market--offices{left:806px;top:236px;background:#9a9a9a}
  .front-brand{left:894px;top:296px;width:256px;height:79px;background:var(--sky);display:flex;align-items:center;justify-content:center}
  .front-brand .name{font-family:"Montserrat",sans-serif;font-weight:800;font-size:40px;letter-spacing:6px;color:var(--purple)}
</style>
</head>
<body>

<section class="spread spread--inside">
  <!-- left panel -->
  <ul class="benefits abs">
    <li>✓ Boost Employee/Clients/ patients Morale</li>
    <li>✓ Increase Productivity</li>
    <li>✓ Support employee Healthy lifestyle</li>
  </ul>
  <p class="intro abs"><span class="tag">ORVIA</span>Markets LLC Micro-Markets and <strong>Vending system allows you to select from hundreds</strong> of healthy, tasty and nutritional balance options. We have healthy snack and fresh produce</p>
  <div class="photo photo--produce abs" role="img" aria-label="Assorted fresh fruit and vegetables"></div>
  <h2 class="section-title abs">EASY CONVENIENT <b>HEALTHY</b></h2>
  <p class="kiosk-copy abs"><span class="initial">O</span>ur Micro Markets are state of Art, with advance technology, credit card, debit card, self-check out Kiosk system, tracks calories and each item before purchase</p>
  <div class="photo photo--shopper abs" role="img" aria-label="Shopper paying at a self-checkout kiosk in a micro-market"></div>

  <!-- middle panel -->
  <div class="facts-panel abs" role="img" aria-label="Faded photo of cheerful people celebrating">
    <div class="facts-head facts-head--cool abs"><b>HOW COOL</b> IS THAT!!!</div>
    <div class="facts-head facts-head--fact abs">FACT:</div>
    <div class="fact fact--1 abs">One-third of U.S Adults (33.8%) are considered obese</div>
    <div class="q q--1 abs">?</div>
    <div class="fact fact--2 abs">Poor Diet can lead to decreased performance and productivity at the office, school &amp; Home</div>
    <div class="q q--2 abs">?</div>
    <div class="fact fact--3 abs"><span>Unhealthy workers cost employers an average of <b>$12,000</b> per year per employee</span></div>
    <div class="q q--3 abs">?</div>
    <p class="cta abs">LETS MAKE A CHANGE AND BECOME HEALTHY,<br>HAPPY SNACK PEOPLE</p>
    <p class="site abs">WWW.ORVIAMARKETS.COM</p>
  </div>

  <!-- right half -->
  <div class="photo photo--market abs" role="img" aria-label="Micro-market with pay kiosks, fresh food, cold drinks, frozen food and snack racks"></div>
  <p class="lead abs"><span class="initial">S</span>marter snacking is proving not to be a short-lived health fad, but rather a top priority among a growing number of consumers</p>
  <h3 class="system-title abs"><b>KIOSK</b> and <b>VENDING</b> SYSTEM</h3>
  <ul class="features features--left abs">
    <li>Remote wireless and Sales monitoring</li>
    <li>Security Monitoring</li>
    <li>Employee user accounts</li>
  </ul>
  <ul class="features features--right abs">
    <li><b>Electronic payment types, Glidepay Wallet, Brisko Pay, Paynest (etc) ...</b></li>
    <li>Accepts Credit Card and debit card, cash and coins, <b>bit coins</b>,</li>
    <li>Accommodates chilled, non-chilled, fresh produce and <b>microwaveable</b></li>
  </ul>
</section>

<section class="spread spread--outside">
  <!-- back cover -->
  <div class="back-cover abs">
    <div class="brand-mark abs"><span class="square"></span><span class="name">ORVIA</span></div>
    <p class="contact-title abs">CONTACT US</p>
    <p class="contact-line abs">CALL TOLL FREE <b>(800) 555-0148</b></p>
  </div>

  <!-- front cover -->
  <div class="photo photo--people abs" role="img" aria-label="Group of smiling friends outdoors in warm sunlight"></div>
  <div class="markets-frame abs"></div>
  <svg class="tail abs" width="56" height="22" viewBox="0 0 56 22" aria-hidden="true">
    <path d="M0 0 L52 0 L52 20 Z" fill="#fff" stroke="#cfe6f5" stroke-width="3"/>
  </svg>
  <div class="headline-box abs">
    <div class="l1">HEALTHY,</div>
    <div class="l2">HAPPY</div>
    <div class="l3">SNACK PEOPLE</div>
  </div>
  <span class="market market--hotels abs">HOTELS</span>
  <span class="market market--colleges abs">COLLEGES/UNIVERSITIES</span>
  <span class="market market--hospitals abs">HOSPITALS</span>
  <span class="market market--offices abs">OFFICES BUILDINGS &amp; MORE</span>
  <div class="front-brand abs"><span class="name">ORVIA</span></div>
</section>

</body>
</html>
```